This is for business cards to display near pieces I am leaving in high traffic retail sites which have agreed to display my work and at craft markets where we intend to sell the works - the business cards should clearly identify:

Wholly Verdant container garden designs by Doreen Falby
Email: Wholly.Verdant@quillpost.example
See Our Full Folio on our Chatterbook page ??????? (yet to be completed - simultaneous design project underway via craft hive)
Ph: 0427 315 608 (9am - 9pm Mon - Sat)
We accept individual and larger orders and are happy to discuss your ideas and requirements. Collection is from Wexbury in Brisbane. Call or email to confirm collection time and address. Free gift wrapping service.

This project has been bundled with a Chatterbook Design Project: http://jobs.crafthive.example/job.aspx?id=517306

I encourage you to submit to both projects and keep designs consistent.
Updates

Hi I am looking for a quick turnaround on a buisiness card and the set up for a complementary chatterbook page with common logo's etc - My business is designing boutique succulent container gardens. If anyone can manage to turn out something appealing by Fri afternoon Australian Eastern time I would be really gateful..... Sorry I am new at this. Doreen

Please note that the deadline on this project is urgent - please submit your entries by Fri 21 November @ Noon Australian Eastern Time. Please use the uploaded template from prontocard. thank you Doreen

Reason: Hi It is not essential that the CB page project be finalised by 21 November - this can be extended to Wed 26 November. However the business card project remains urgent with a deadline of 21 November. thanks Doreen

Hi Although I would like these business cards ASAP (eg. by 21 November) - If I get a great result with an integrated design between the chatterbook page and the business cards then I am prepared to wait until Wed 26 November. Please note that the fee for this project has also been increased by $75. thanks Doreen

Target Market(s)

Adults based in western speaking countries aged 20 to 70 that enjoy gardening, live in apartments or are looking for an unusual gift for a loved one or friend. Our pricepoints will be between $25 - $200 AUD.

Industry/Entity Type

Retail

Font styles to use
Script

Colors
b7a5cd
85abd2
f9d9e8
8869ae
fee18a
86cfc6
ffc213
cadf82
e567a6

Requirements
Must have
• I would like the Blue Mauve Echinvera Rose on the backside of the business Card and to form the basis of the logo for both the chatterbook page and the business card- but it was taken from imagebarn 456 QXL and although I have paid for the correct licence - it would be proper to acknowledge the photographer noted as "riddlefox" somewhere on the business card and on the CB page.

I would like to convey the message that we are a small boutique business that design compact succulent gardens using our imagination to pair the natural qualities of the plants with their containers. Wherever possible we carefully select upcycled, quirky, vintage and recycled materials for our containers so that each piece is unique. Succulents require very little maintenance and in Spring and Summer will delight and suprise you with their unexpected and sometimes quite spectacular display of flowers. We also offer a small range of delightful individually handcrafted garden art windchimes and mobiles also made from carefully selected vintage items.
Nice to have
• If you have any brainwaves - let us know and we can negotiate with you. Unfortunately I dont have any pics of the mobiles - which are fab - will see if I can get some loaded within the next 24 hours.
Should not have
• Any mention of cactus or images of them - we dont sell with them or work with them if we can help it - their spikes hurt and they are not child friendly.

I have included a bunch of files - just select those you think might work well as samples of our work for our chatterbook page and get rid of the blurry ones - my eyes are not very good and I was using a DSLR camera which is very difficult now cos I have trouble manually focussing.

```html
<!DOCTYPE html>
<html lang="en">
<head>
<meta charset="utf-8">
<title>Wholly Verdant – Business Card</title>
<link rel="stylesheet" href="https://fonts.googleapis.com/css2?family=Lobster&family=Open+Sans:wght@400&display=swap">
<style>
  :root {
    --page: #ffffff;
    --frame: #cfe3b5;
    --teal: #86cfc6;
    --teal-deep: #7fcbc2;
    --leaf: #cadf82;
    --band: #d4e8c3;
    --ink: #4f4f4f;
  }
  * { box-sizing: border-box; margin: 0; padding: 0; }
  html, body {
    width: 981px; height: 1200px; overflow: hidden;
    background: var(--page);
  }
  .canvas { position: relative; width: 981px; height: 1200px; }

  /* Front side */
  .card-front {
    position: absolute; left: 60px; top: 31px;
    width: 869px; height: 536px;
    border: 2px solid var(--frame);
    background: var(--page);
  }
  .logo-art {
    position: absolute; left: 297px; top: 32px;
    width: 270px; height: 240px;
    border-radius: 50%;
    background: radial-gradient(circle at 50% 50%, #e4f0d0 0%, var(--leaf) 45%, var(--teal) 100%);
  }
  .brand-name {
    position: absolute; left: 0; right: 0; top: 286px;
    text-align: center;
    font-family: "Lobster", cursive;
    font-size: 54px; line-height: 70px;
    color: var(--teal);
  }
  .contact-list {
    position: absolute; left: 0; right: 0; top: 401px;
    list-style: none; text-align: center;
    font-family: "Open Sans", sans-serif;
    font-size: 21px; line-height: 31.5px;
    color: var(--ink);
  }
  .contact-list li { display: flex; justify-content: center; align-items: center; gap: 9px; }
  .contact-icon { width: 17px; height: 17px; flex: none; }
  .contact-square { width: 14px; height: 14px; background: var(--ink); flex: none; }

  /* Back side */
  .card-back {
    position: absolute; left: 60px; top: 610px;
    width: 869px; height: 536px;
    display: flex; flex-direction: column;
  }
  .pattern {
    background: linear-gradient(135deg, var(--teal) 0%, #bfe6e1 50%, var(--teal) 100%);
  }
  .pattern-top { height: 178px; }
  .pattern-bottom { height: 161px; }
  .info-band {
    height: 197px;
    background: var(--band);
    display: flex; align-items: flex-start; justify-content: center;
    padding-top: 20px;
    font-family: "Open Sans", sans-serif;
    font-size: 21px; line-height: 31.5px;
    color: var(--ink); text-align: center;
  }
</style>
</head>
<body>
<main class="canvas">
  <section class="card-front">
    <div class="logo-art" role="img" aria-label="Brand emblem: a layered succulent rosette in teal and lime green"></div>
    <h1 class="brand-name">Wholly Verdant</h1>
    <ul class="contact-list">
      <li>
        <svg class="contact-icon" viewBox="0 0 16 16" aria-hidden="true">
          <path d="M1 6 L8 1 L15 6 V15 H1 Z" fill="#4f4f4f"/>
          <path d="M1 6 L8 11 L15 6" fill="none" stroke="#fff" stroke-width="1.4"/>
        </svg>
        Wholly.Verdant@quillpost.example
      </li>
      <li><span class="contact-square" aria-hidden="true"></span>chatterbook/ Wholly.Verdant</li>
      <li>
        <svg class="contact-icon" viewBox="0 0 16 16" aria-hidden="true">
          <path d="M1 5 Q8 0 15 5 L13 7 L11 5.5 L5 5.5 L3 7 Z" fill="#4f4f4f"/>
          <path d="M4 8 L12 8 L14 14 L2 14 Z" fill="#4f4f4f"/>
          <circle cx="8" cy="11" r="1.8" fill="#fff"/>
        </svg>
        0427 315 608 (9am - 9pm Mon - Sat)
      </li>
    </ul>
  </section>

  <section class="card-back">
    <div class="pattern pattern-top" role="img" aria-label="Decorative pattern of white succulent rosettes outlined on teal"></div>
    <div class="info-band">
      <p>We accept individual and larger orders and are happy to<br>
      discuss your ideas and requirements.<br>
      Collection is from Wexbury in Brisbane.<br>
      Call or email to confirm collection time and address.<br>
      Free gift wrapping service.</p>
    </div>
    <div class="pattern pattern-bottom" role="img" aria-label="Decorative pattern of white succulent rosettes outlined on teal"></div>
  </section>
</main>
</body>
</html>
```